Commercial construction contractor website.

We need a website that contains About Us, Contact info, Services, Project pictures and Industry News section

Target Market(s)

I'm building industral/flex spaces/commercial.

Industry/Entity Type

Commercial/industrial construction

Coding

Coded - Design and coding required

Number of Pages Required

5+ page

Font styles to use
Other font styles liked:
• The logo font is Microgramma Pro

Requirements
Must have
• Must have correct company name spelling: Dunmore Ridge Construction
Nice to have
• I do like to see our logo design implemented in the design
Should not have
• Please do not show big city pictures and business suit people. We are a commercial construction company

```html
<!DOCTYPE html>
<html lang="en">
<head>
<meta charset="utf-8">
<title>Dunmore Ridge Construction</title>
<link href="https://fonts.googleapis.com/css2?family=Michroma&family=Exo+2:wght@600;700;800&family=Hind:wght@400;500;600&display=swap" rel="stylesheet">
<style>
:root{
  --navy:#0b2c6b;
  --navy-deep:#082258;
  --blue:#1a6fb5;
  --blue-bright:#1560b0;
  --pale:#d6e6f3;
  --grey-head:#6b6b6b;
  --text:#333;
  --muted:#8a8a8a;
  --footer:#141922;
  --white:#fff;
}
*{margin:0;padding:0;box-sizing:border-box}
html,body{width:1200px;height:5063px;overflow:hidden}
body{position:relative;background:var(--white);font-family:"Hind",sans-serif;color:var(--text)}
.abs{position:absolute}
.backdrop{position:absolute;left:0;top:0;width:1200px;height:5063px}

/* header */
.site-header{position:absolute;left:0;top:0;width:1200px;height:114px;background:var(--white)}
.brand{position:absolute;left:143px;top:38px;display:flex;align-items:center;gap:8px;font-family:"Michroma",sans-serif;font-size:13px;color:var(--navy);letter-spacing:.5px}
.brand-dot{width:26px;height:26px;border-radius:50%;background:var(--navy)}
.callout{position:absolute;left:648px;top:16px;display:flex;align-items:center;gap:8px;font-size:17px;font-weight:600;color:#7a7a7a}
.callout b{color:#7a7a7a;font-weight:600}
.callout svg{width:32px;height:32px}
.nav{position:absolute;top:72px;left:0;font-size:13px;font-weight:600;color:#333}
.nav span{position:absolute;white-space:nowrap}
.login{position:absolute;left:974px;top:61px;width:81px;height:39px;border-radius:20px;background:var(--navy);color:#fff;font-size:13px;font-weight:600;display:flex;align-items:center;justify-content:center}

/* hero */
.hero-title{position:absolute;left:0;width:1200px;text-align:center;color:#fff;font-family:"Michroma",sans-serif}
.hero-title.main{top:302px;font-size:52px;letter-spacing:1px}
.hero-title.sub{top:366px;font-size:32px;display:flex;align-items:center;justify-content:center;gap:18px}
.hero-title.sub i{display:block;width:80px;height:4px;background:#fff}
.play{position:absolute;left:556px;top:460px;width:86px;height:86px}

/* headings */
.section-title{position:absolute;left:0;width:1200px;text-align:center;font-family:"Exo 2",sans-serif;font-weight:800;font-size:52px;letter-spacing:1px;color:var(--grey-head)}
.section-title.light{color:#fff}
.btn{position:absolute;left:518px;width:162px;height:47px;border-radius:24px;font-size:15px;font-weight:600;display:flex;align-items:center;justify-content:center}
.btn.dark{background:var(--navy);color:#fff}
.btn.light{background:#fff;color:var(--navy)}

/* welcome */
.welcome-mark{position:absolute;left:579px;top:776px;width:40px;height:40px;border-radius:50%;background:var(--navy)}
.welcome-copy{position:absolute;left:236px;top:975px;width:728px;text-align:center;font-size:13px;line-height:29px;color:#555}

/* services */
.service-label{position:absolute;font-family:"Exo 2",sans-serif;font-weight:700;font-size:17px;line-height:28px;color:#333;white-space:nowrap}
.service-label.left{text-align:right}
.service-icon{position:absolute;width:80px;height:80px;border-radius:50%;display:flex;align-items:center;justify-content:center}
.service-icon.blue{background:var(--blue)}
.service-icon.navy{background:var(--navy)}
.service-icon svg{width:36px;height:36px}
.hub-name{position:absolute;left:462px;top:2010px;width:274px;text-align:center;font-family:"Michroma",sans-serif;font-size:19px;line-height:30px;color:var(--navy)}

/* gallery */
.photo{position:absolute;width:293px;height:244px}

/* news */
.news-card{position:absolute;left:299px;width:604px;height:248px;background:#fff;border-radius:30px;border:2px solid #c7d6e6}
.news-photo{position:absolute;left:2px;top:2px;width:236px;height:240px;border-radius:28px 0 0 28px}
.news-date{position:absolute;left:268px;top:28px;font-size:12px;font-weight:600;color:var(--navy)}
.news-title{position:absolute;left:268px;top:58px;width:310px;font-family:"Exo 2",sans-serif;font-size:16px;font-weight:700;line-height:24px;color:#222}
.news-body{position:absolute;left:268px;top:116px;width:300px;font-size:12px;line-height:23px;color:#999}
.news-more{position:absolute;left:268px;top:206px;font-size:14px;font-weight:600;color:var(--blue-bright)}

/* contact */
.label-head{position:absolute;font-size:14px;font-weight:600;color:#fff}
.field{position:absolute;background:#fff;font-size:10px;color:#777;padding:7px 10px}
.submit{position:absolute;left:648px;top:4892px;width:76px;height:28px;border-radius:14px;background:var(--blue-bright);color:#fff;font-size:11px;font-weight:600;display:flex;align-items:center;justify-content:center}
.info-row{position:absolute;left:795px;display:flex;align-items:center;gap:14px;font-size:11px;line-height:15px;color:#ddd}
.info-icon{width:34px;height:34px;border:2px solid #fff;border-radius:50%;display:flex;align-items:center;justify-content:center;flex:none}
.info-icon svg{width:15px;height:15px}
.social{position:absolute;top:4887px;width:26px;height:26px;border-radius:50%}
.footer-rule{position:absolute;left:0;top:4979px;width:1200px;height:1px;background:#2a303c}
.copyright{position:absolute;left:0;top:5012px;width:1200px;text-align:center;font-size:11px;color:#ccc}
</style>
</head>
<body>

<svg class="backdrop" viewBox="0 0 1200 5063" aria-hidden="true">
  <defs>
    <linearGradient id="heroTone" x1="0" y1="0" x2="1" y2="1">
      <stop offset="0" stop-color="#1a3f9a"/>
      <stop offset=".5" stop-color="#1238a8"/>
      <stop offset="1" stop-color="#0a1f6a"/>
    </linearGradient>
    <linearGradient id="galleryTone" x1="0" y1="0" x2="0" y2="1">
      <stop offset="0" stop-color="#0a2668"/>
      <stop offset="1" stop-color="#0e4b9c"/>
    </linearGradient>
    <linearGradient id="siteTone" x1="0" y1="0" x2="1" y2="0">
      <stop offset="0" stop-color="#e3ecf6"/>
      <stop offset=".5" stop-color="#a9c0de"/>
      <stop offset="1" stop-color="#2d5fa8"/>
    </linearGradient>
    <linearGradient id="siteFade" x1="0" y1="0" x2="0" y2="1">
      <stop offset="0" stop-color="#fff" stop-opacity="0"/>
      <stop offset=".25" stop-color="#fff" stop-opacity=".35"/>
      <stop offset=".55" stop-color="#fff" stop-opacity="1"/>
      <stop offset="1" stop-color="#fff" stop-opacity="1"/>
    </linearGradient>
    <mask id="siteMask" maskUnits="userSpaceOnUse" x="143" y="1060" width="912" height="580">
      <rect x="143" y="1060" width="912" height="580" fill="url(#siteFade)"/>
    </mask>
    <clipPath id="welcomeHex"><polygon points="599,690 1055,953 1055,1375 599,1622 143,1375 143,953"/></clipPath>
  </defs>
  <polygon points="0,114 1200,114 1200,600 820,812 599,674 380,812 0,600" fill="url(#heroTone)"/>
  <polygon points="599,690 1055,953 1055,1375 599,1622 143,1375 143,953" fill="var(--pale)"/>
  <g clip-path="url(#welcomeHex)">
    <rect x="143" y="1060" width="912" height="580" fill="url(#siteTone)" mask="url(#siteMask)"/>
  </g>
  <polygon points="0,2553 340,2357 589,2498 860,2340 1200,2530 1200,3340 786,3560 599,3405 428,3560 0,3340" fill="url(#galleryTone)"/>
  <polygon points="0,4600 330,4400 870,4400 1200,4600 1200,5063 0,5063" fill="var(--footer)"/>
  <polygon points="599,3422 1055,3692 1055,4290 599,4545 143,4290 143,3692" fill="var(--pale)" stroke="#fff" stroke-width="14"/>
</svg>

<div role="img" aria-label="Hero photo of a steel frame industrial building under construction" class="abs" style="left:0;top:114px;width:1200px;height:500px"></div>
<div role="img" aria-label="Photo of a flex space building shell under construction" class="abs" style="left:143px;top:1240px;width:912px;height:380px"></div>

<header class="site-header">
  <div class="brand"><span class="brand-dot"></span>DUNMORE RIDGE</div>
  <div class="callout">
    <svg viewBox="0 0 32 32"><circle cx="16" cy="16" r="14" fill="none" stroke="#0b2c6b" stroke-width="2"/><path d="M11 9c1-1 2-1 3 0l2 3c.5 1 0 2-1 2.5 1 2 2.5 3.5 4.5 4.5.5-1 1.5-1.5 2.5-1l3 2c1 1 1 2 0 3-2 2-5 1.5-9-2.5S9 11 11 9z" fill="#0b2c6b"/></svg>
    CALL US : <b>1 555 014 2290</b>
  </div>
  <nav class="nav">
    <span style="left:393px">HOME</span>
    <span style="left:458px">ABOUT US</span>
    <span style="left:552px">CONTACT</span>
    <span style="left:638px">SERVICES</span>
    <span style="left:729px">PROJECTS</span>
    <span style="left:823px">INDUSTRY NEWS</span>
  </nav>
  <div class="login">LOGIN</div>
</header>

<section class="hero">
  <h1 class="hero-title main">DUNMORE RIDGE</h1>
  <div class="hero-title sub"><i></i>CONSTRUCTION<i></i></div>
  <svg class="play" viewBox="0 0 86 86"><circle cx="43" cy="43" r="39" fill="none" stroke="#fff" stroke-width="6"/><polygon points="34,26 62,43 34,60" fill="#fff"/></svg>
</section>

<section class="welcome">
  <div class="welcome-mark"></div>
  <h2 class="section-title" style="top:872px">WELCOME</h2>
  <p class="welcome-copy">Lorem ipsum dolor sit amet, consectetur adipiscing elit, sed do eiusmod tempor incididunt ut labore et dolore magna aliquis ipsum suspendisse ultrices grav viverra maecenas accumsan lacus vel facilisis. Lorem ipsum dolor sit amet, consectetur adipiscing elit, sed do eiusmod tempor incididunt ut labore et dolore magna aliquis ipsum suspendisse ultrices grav viverra maecenas accumsan lacus vel facilisisrem ipsum dolor sit amet, consectetur adipiscinempm suspendisse ultrices grav viverra maecenas accumsan lacus vel facilisis.</p>
  <div class="btn dark" style="top:1153px">READ MORE</div>
</section>

<section class="services">
  <h2 class="section-title" style="top:1705px">SERVICES</h2>
  <svg class="abs" style="left:420px;top:1864px" width="360" height="360" viewBox="0 0 360 360" aria-hidden="true">
    <defs><filter id="hubShadow" x="-20%" y="-20%" width="140%" height="140%"><feDropShadow dx="0" dy="3" stdDeviation="8" flood-color="#8aa0bb" flood-opacity=".45"/></filter></defs>
    <circle cx="180" cy="180" r="165" fill="none" stroke="#1a6fb5" stroke-width="4"/>
    <circle cx="180" cy="180" r="137" fill="#fff" filter="url(#hubShadow)"/>
    <g fill="#fff" stroke="#0b2c6b" stroke-width="3">
      <circle cx="56" cy="71" r="6"/><circle cx="304" cy="71" r="6"/>
      <circle cx="14" cy="175" r="6"/><circle cx="346" cy="175" r="6"/>
      <circle cx="58" cy="297" r="6"/><circle cx="302" cy="297" r="6"/>
    </g>
  </svg>
  <div class="hub-name">DUNMORE<br>RIDGE</div>

  <div class="service-label left" style="right:835px;top:1873px">Accusantium dolor<br>oluptatemque</div>
  <div class="service-icon blue" style="left:376px;top:1861px"><svg viewBox="0 0 36 36" fill="#fff"><rect x="5" y="8" width="26" height="23" rx="2"/><rect x="10" y="4" width="3" height="7"/><rect x="23" y="4" width="3" height="7"/><g fill="#1a6fb5"><rect x="9" y="16" width="4" height="3"/><rect x="16" y="16" width="4" height="3"/><rect x="23" y="16" width="4" height="3"/><rect x="9" y="23" width="4" height="3"/><rect x="16" y="23" width="4" height="3"/><rect x="23" y="23" width="4" height="3"/></g></svg></div>

  <div class="service-icon navy" style="left:738px;top:1861px"><svg viewBox="0 0 36 36" fill="#fff"><polygon points="18,4 33,11 3,11"/><rect x="6" y="13" width="3" height="14"/><rect x="12" y="13" width="3" height="14"/><rect x="21" y="13" width="3" height="14"/><rect x="27" y="13" width="3" height="14"/><rect x="3" y="28" width="30" height="4"/></svg></div>
  <div class="service-label" style="left:827px;top:1873px">Nemo enim<br>ipsam voluptatem</div>

  <div class="service-label left" style="right:898px;top:2018px">Ut enimminimeniam<br>quis nostrum</div>
  <div class="service-icon navy" style="left:310px;top:2007px"><svg viewBox="0 0 36 36" fill="#fff"><rect x="10" y="4" width="16" height="28"/><g fill="#0b2c6b"><rect x="13" y="8" width="3" height="3"/><rect x="20" y="8" width="3" height="3"/><rect x="13" y="14" width="3" height="3"/><rect x="20" y="14" width="3" height="3"/><rect x="13" y="20" width="3" height="3"/><rect x="20" y="20" width="3" height="3"/><rect x="16" y="26" width="4" height="6"/></g></svg></div>

  <div class="service-icon blue" style="left:781px;top:2007px"><svg viewBox="0 0 36 36" fill="#fff"><circle cx="18" cy="12" r="5"/><circle cx="8" cy="14" r="3.5"/><circle cx="28" cy="14" r="3.5"/><path d="M9 28c0-6 4-9 9-9s9 3 9 9z"/><path d="M2 26c0-4 3-6 6-6 1 0 2 0 3 1-2 1-3 3-3 5z"/><path d="M34 26c0-4-3-6-6-6-1 0-2 0-3 1 2 1 3 3 3 5z"/></svg></div>
  <div class="service-label" style="left:871px;top:2018px">Sed ut perspiciatis<br>unde omnis iste</div>

  <div class="service-label left" style="right:831px;top:2164px">Duis aute irure dolor<br>in reprehenderit</div>
  <div class="service-icon blue" style="left:380px;top:2152px"><svg viewBox="0 0 36 36" fill="#fff"><rect x="7" y="4" width="14" height="20" rx="1"/><rect x="14" y="11" width="15" height="21" rx="1" stroke="#1a6fb5" stroke-width="2"/></svg></div>

  <div class="service-icon navy" style="left:738px;top:2152px"><svg viewBox="0 0 36 36" fill="#fff"><circle cx="13" cy="20" r="8"/><circle cx="13" cy="20" r="3" fill="#0b2c6b"/><circle cx="26" cy="11" r="6"/><circle cx="26" cy="11" r="2" fill="#0b2c6b"/><circle cx="27" cy="26" r="4"/></svg></div>
  <div class="service-label" style="left:831px;top:2164px">Quis autem vel eum iure<br>reprehenderit</div>
</section>

<section class="gallery">
  <h2 class="section-title light" style="top:2589px">PROJECT GALLERY</h2>
  <div class="photo" role="img" aria-label="Steel stud wall framing inside a building" style="left:143px;top:2710px;background:linear-gradient(90deg,#9aa3ae,#d7dce2 50%,#7d8793)"></div>
  <div class="photo" role="img" aria-label="Crew in safety vests walking a concrete slab site" style="left:454px;top:2710px;background:linear-gradient(160deg,#8a8580,#c9c2b6 60%,#a69d90)"></div>
  <div class="photo" role="img" aria-label="Workers in harnesses erecting a steel roof frame" style="left:764px;top:2710px;background:linear-gradient(160deg,#e6edf5,#a8b7c8 50%,#5f6f82)"></div>
  <div class="photo" role="img" aria-label="Roofer fastening metal roof panels" style="left:143px;top:2973px;background:linear-gradient(135deg,#f3f0ea,#b9bcc2 50%,#5b636e)"></div>
  <div class="photo" role="img" aria-label="Precast concrete frame with a lift on site" style="left:454px;top:2973px;background:linear-gradient(180deg,#5c8ed0,#e4e6e8 45%,#b8b3a8)"></div>
  <div class="photo" role="img" aria-label="Tower crane over a building wrapped in scaffolding" style="left:764px;top:2973px;background:linear-gradient(180deg,#3f7fd0,#2a60b0 55%,#2a4f8e)"></div>
  <div class="btn light" style="top:3276px">VIEW MORE</div>
</section>

<section class="news">
  <h2 class="section-title" style="top:3628px">INDUSTRY NEWS</h2>
  <article class="news-card" style="top:3747px">
    <div class="news-photo" role="img" aria-label="Steel frame structure viewed from below" style="background:linear-gradient(160deg,#2b5fb0,#4e86cc 50%,#1c3f7a)"></div>
    <div class="news-date">Aug,2019</div>
    <h3 class="news-title">Sed ut perspiciatis unde omnis<br>iste natus error</h3>
    <p class="news-body">Ut enim ad minima veniam, quis nostreierci tationem ullam corporis suscipit laboriosan isi ut aliquid ex ea eprehenderitq utate velit .</p>
    <div class="news-more">READ MORE</div>
  </article>
  <article class="news-card" style="top:4010px">
    <div class="news-photo" role="img" aria-label="Crew tying rebar on a concrete deck" style="background:linear-gradient(160deg,#6d7580,#9aa1aa 50%,#4d5560)"></div>
    <div class="news-date">Aug,2019</div>
    <h3 class="news-title">Sed ut perspiciatis unde omnis<br>iste natus error</h3>
    <p class="news-body">Ut enim ad minima veniam, quis nostreierci tationem ullam corporis suscipit laboriosan isi ut aliquid ex ea eprehenderitq utate velit .</p>
    <div class="news-more">READ MORE</div>
  </article>
  <div class="btn dark" style="top:4329px">VIEW MORE</div>
</section>

<footer class="contact">
  <h2 class="section-title" style="top:4585px;color:#7a7a7a">CONTACT US</h2>
  <div class="label-head" style="left:181px;top:4686px">Get In Touch:</div>
  <div class="field" style="left:183px;top:4725px;width:265px;height:28px">NAME :</div>
  <div class="field" style="left:459px;top:4725px;width:266px;height:28px">PHONE :</div>
  <div class="field" style="left:183px;top:4767px;width:542px;height:28px">EMAIL :</div>
  <div class="field" style="left:183px;top:4806px;width:542px;height:67px">MESSAGE :</div>
  <div class="submit">SUBMIT</div>

  <div class="label-head" style="left:795px;top:4686px">Contact Information</div>
  <div class="info-row" style="top:4726px"><span class="info-icon"><svg viewBox="0 0 16 16" fill="#fff"><path d="M8 1a5 5 0 0 0-5 5c0 4 5 9 5 9s5-5 5-9a5 5 0 0 0-5-5zm0 7a2 2 0 1 1 0-4 2 2 0 0 1 0 4z"/></svg></span><span>122,quia consequuntur magni<br>dolores eos qui</span></div>
  <div class="info-row" style="top:4777px"><span class="info-icon"><svg viewBox="0 0 16 16" fill="#fff"><path d="M4 1c1-1 2 0 2.5 1l1 2c.3 1-.3 1.5-1 2 .8 1.6 2 2.8 3.5 3.5.5-.7 1-1.3 2-1l2 1c1 .5 2 1.5 1 2.5-2 2.5-5 1-8-2S1.5 3 4 1z"/></svg></span><span>Call Us : 1 555 014 2290</span></div>
  <div class="info-row" style="top:4820px"><span class="info-icon"><svg viewBox="0 0 16 16" fill="#fff"><rect x="1" y="3" width="14" height="10" rx="1"/><path d="M1 4l7 5 7-5" fill="none" stroke="#141922" stroke-width="1.5"/></svg></span><span>info@dunmoreridgebuild.com</span></div>

  <span class="social" style="left:796px;background:#3b5a9a"></span>
  <span class="social" style="left:830px;background:#1da1f2"></span>
  <span class="social" style="left:865px;background:#e02d2d"></span>
  <span class="social" style="left:898px;background:#b07a4a"></span>
  <span class="social" style="left:932px;background:#1d77b5"></span>

  <div class="footer-rule"></div>
  <p class="copyright">Copyrights © 2022, Dunmore Ridge Construction. All Rights Reserved. &nbsp;|&nbsp; Privacy policy</p>
</footer>

</body>
</html>
```